New Website for Corriveld House at www.corriveld.com.au

A new logo has been designed (through pixel forum) and we now want to align the look and feel of our website at www.corriveld.com.au to the new logo. The content and page names (e.g. Grounds) will remain largely unchanged for the new site, so please submit a new look "Home" page, using our new logo, current text and any photos you choose from the existing gallery at our website. I have also attached the current "Home" page photos.

Industry/Entity Type

Accommodation

Number of Pages Required

1 page

Requirements
Must have
• Logo to be presented on white background.

```html
<!DOCTYPE html>
<html lang="en">
<head>
<meta charset="utf-8">
<title>Corriveld House – Home</title>
<link href="https://fonts.googleapis.com/css2?family=PT+Serif:wght@400;700&family=Roboto:wght@400;500;700&display=swap" rel="stylesheet">
<style>
:root{
  --ink:#1b1b1b;
  --muted:#777;
  --white:#fff;
  --sea-dark:#0f3566;
  --sea:#2a6aa8;
  --sea-light:#5b95c9;
  --band:#1177c2;
  --black:#000;
  --footer:#050505;
  --footer-bottom:#0d0d0d;
  --gold:#e6b800;
  --line:#c9c9c9;
}
*{margin:0;padding:0;box-sizing:border-box}
html,body{width:1200px;height:2995px;overflow:hidden;background:var(--white)}
body{position:relative;font-family:'Roboto',Arial,sans-serif;color:var(--ink)}
.serif{font-family:'PT Serif',Georgia,serif}
.abs{position:absolute}

/* hero */
.hero{left:0;top:0;width:1200px;height:675px;background:linear-gradient(160deg,var(--sea-light) 0%,var(--sea) 40%,var(--sea-dark) 100%)}
.brand{left:50px;top:0;width:172px;height:116px;background:var(--white);display:flex;align-items:center;justify-content:center;gap:8px}
.brand-dot{width:14px;height:14px;border-radius:50%;background:#1f8ed3}
.brand-name{font-family:'PT Serif',Georgia,serif;font-size:22px;color:#1f8ed3}
.nav{left:324px;top:84px;display:flex;gap:0;align-items:center}
.nav a{color:var(--white);text-decoration:none;font-size:12px;font-weight:700;letter-spacing:.3px;padding:8px 12px;text-transform:uppercase}
.nav a.current{border:2px solid var(--white)}
.hero-title{left:0;width:1200px;top:234px;text-align:center;color:var(--white);font-size:36px;font-family:'PT Serif',Georgia,serif}
.hero-sub{left:0;width:1200px;top:284px;text-align:center;color:var(--white);font-size:15px;letter-spacing:1px;font-family:'PT Serif',Georgia,serif}
.btn-explore{left:520px;top:360px;width:156px;height:42px;border:3px solid var(--white);color:var(--white);display:flex;align-items:center;justify-content:center;font-family:'PT Serif',Georgia,serif;font-size:16px}

/* welcome panel */
.panel{left:58px;top:514px;width:1082px;height:200px;background:var(--white)}
.ghost{left:0;width:1200px;top:560px;text-align:center;font-family:'PT Serif',Georgia,serif;font-size:110px;color:#f3f3f3;letter-spacing:6px}
.h-title{left:0;width:1200px;text-align:center;font-family:'PT Serif',Georgia,serif;font-size:28px;color:var(--ink)}
.h-sub{left:0;width:1200px;text-align:center;font-size:13px;letter-spacing:3px;color:#555;text-transform:uppercase}
.divider{left:530px;width:140px;height:14px}
.intro{left:150px;width:900px;top:798px;text-align:center;font-size:12px;line-height:18px;color:#666}

/* cards */
.card{top:950px;width:342px;height:446px;color:var(--white)}
.card .photo{position:absolute;inset:0}
.card .label{position:absolute;left:42px;top:28px;font-family:'PT Serif',Georgia,serif;font-size:26px}
.card .kind{position:absolute;left:42px;top:62px;font-family:'PT Serif',Georgia,serif;font-size:16px}
.card .caption{position:absolute;left:24px;bottom:24px;font-size:22px;font-weight:700;text-transform:uppercase}
.card .blurb{position:absolute;left:24px;right:60px;bottom:26px;font-size:13px;line-height:18px}

/* offer */
.offer-text{left:0;width:1200px;top:1544px;text-align:center;font-size:12px;color:#555}
.btn-rooms{left:518px;top:1594px;width:160px;height:38px;border:1px solid #999;display:flex;align-items:center;justify-content:center;font-size:12px;font-weight:500;text-transform:uppercase;color:var(--ink)}

/* suite band */
.band{left:0;top:1690px;width:1200px;height:506px;background:var(--band)}
.suite{left:150px;top:1758px;width:462px;height:366px;background:var(--black);color:var(--white)}
.suite h3{position:absolute;left:42px;top:40px;font-family:'PT Serif',Georgia,serif;font-weight:400;font-size:24px}
.suite .comments{position:absolute;left:42px;top:78px;font-size:13px;color:var(--gold)}
.suite .shares{position:absolute;left:42px;top:108px;display:flex;gap:14px}
.suite .shares span{width:10px;height:10px;background:#888}
.suite p{position:absolute;left:42px;right:40px;top:136px;font-size:13px;line-height:20px;color:#aaa}
.suite .more{position:absolute;left:50px;top:236px;font-size:15px;text-transform:uppercase}
.suite-photo{left:612px;top:1758px;width:436px;height:366px;background:linear-gradient(180deg,#7fa6c9 0%,#c9785a 38%,#e0c870 58%,#5e7a4a 80%,#8a8a84 100%)}

/* testimonials */
.avatar{left:556px;top:2384px;width:88px;height:88px;border-radius:50%;background:#e8c7a8}
.person{left:0;width:1200px;top:2490px;text-align:center;font-size:17px;color:#333}
.quote{left:140px;width:920px;top:2526px;text-align:center;font-size:12px;line-height:20px;color:#777}

/* footer */
.footer{left:0;top:2652px;width:1200px;height:260px;background:var(--footer)}
.footer-brand{left:0;width:1200px;top:2682px;text-align:center;font-family:'PT Serif',Georgia,serif;font-size:30px;color:#aaa}
.fcol{top:2768px;color:#bbb;display:flex;gap:18px}
.fcol svg{flex:none;margin-top:6px}
.fcol h4{font-size:13px;font-weight:500;letter-spacing:.5px;margin-bottom:8px;color:#ccc}
.fcol div{font-size:11px;line-height:18px;color:#999}
.legal{left:0;top:2912px;width:1200px;height:83px;background:var(--footer-bottom);color:#999;font-size:11px;text-align:center;padding-top:30px}
</style>
</head>
<body>

<div class="abs hero" role="img" aria-label="Overwater villas and deck at dusk over a calm blue sea"></div>
<div class="abs brand"><span class="brand-dot"></span><span class="brand-name">Corriveld</span></div>
<nav class="abs nav">
  <a class="current">Main</a><a>Mansion</a><a>Bedrooms</a><a>Options</a><a>Froq and Toad</a><a>Grounds</a><a>Location</a><a>Gallery</a><a>Contact</a>
</nav>
<h1 class="abs hero-title">Welcome to Corriveld House</h1>
<div class="abs hero-sub">IN DOOR &amp; OUR DOOR</div>
<div class="abs btn-explore">EXPLORE</div>

<div class="abs panel"></div>
<div class="abs ghost">WELCOME</div>
<h2 class="abs h-title" style="top:612px">CORRIVELD HOUSE</h2>
<div class="abs h-sub" style="top:648px">One of the best places to do.. everything</div>
<svg class="abs divider" style="top:710px" viewBox="0 0 140 14"><line x1="0" y1="7" x2="140" y2="7" stroke="#333" stroke-width="1.5"/><rect x="64" y="1" width="12" height="12" fill="#333" transform="rotate(45 70 7)"/></svg>
<h2 class="abs h-title" style="top:748px">PROVIDING QUALITY SERVICES SINCE '98.</h2>
<p class="abs intro">Creepeth creepeth tree moving image unto creepeth above you there let to brought over seas cattle he great give, day creepeth you'll their sea called don't their given dry, make said so lesser divided, firmament fill fowl night second cattle over sixth evening god moveth day stars good evening years you're beginning have you'll fowl. Rule life spirit, whales him</p>

<div class="abs card" style="left:58px">
  <div class="photo" role="img" aria-label="Hot stone massage on a bare back" style="background:linear-gradient(160deg,#c98a52,#e6c3a0 55%,#a86a3c)"></div>
  <div class="label">Corriveld</div><div class="kind">Spa</div>
  <div class="blurb">Velora hosts an amazing place to relax; we call it paradise you may call it Velora Spa. We would love to introduce you to this amazing relaxing and refreshing experience.</div>
</div>
<div class="abs card" style="left:428px">
  <div class="photo" role="img" aria-label="Hand lifting a steel dumbbell in the gym" style="background:linear-gradient(160deg,#5a4a44,#8a8f99 50%,#2b2b30)"></div>
  <div class="label">Corriveld</div><div class="kind">Spa</div>
  <div class="caption">Gym</div>
</div>
<div class="abs card" style="left:798px">
  <div class="photo" role="img" aria-label="Seafood paella in a pan with fork and knife" style="background:linear-gradient(160deg,#a7a9b3,#8b8e99 45%,#6a5a52 70%,#b0b2ba)"></div>
  <div class="label">Corriveld</div><div class="kind">Restaurant</div>
  <div class="caption">Restaurant</div>
</div>

<h2 class="abs h-title" style="top:1456px">GET 15% OFF TODAY</h2>
<svg class="abs divider" style="top:1510px" viewBox="0 0 140 14"><line x1="0" y1="7" x2="140" y2="7" stroke="#333" stroke-width="1.5"/><rect x="64" y="1" width="12" height="12" fill="#333" transform="rotate(45 70 7)"/></svg>
<div class="abs offer-text">Buy now the most awesome offer, and secure your summer vacations on time</div>
<div class="abs btn-rooms">View our rooms</div>

<div class="abs band"></div>
<div class="abs suite">
  <h3>DULUXE KING SUITE</h3>
  <div class="comments">5 Comment</div>
  <div class="shares"><span></span><span></span><span></span></div>
  <p>Lights after was seas under saw fowl without greater, male lights bearing over. Under sixth great multiply isn't under. Own moving won't they're beginning god face greater they're and creature created day first their also moving lesser they're don't.</p>
  <div class="more">Read more</div>
</div>
<div class="abs suite-photo" role="img" aria-label="Yellow house with red tiled roof, palm tree and driveway"></div>

<h2 class="abs h-title" style="top:2228px;font-size:24px">TESTIMONIALS</h2>
<div class="abs h-sub" style="top:2268px">Lovely people - lovely experience</div>
<svg class="abs divider" style="top:2318px" viewBox="0 0 140 14"><line x1="0" y1="7" x2="140" y2="7" stroke="#333" stroke-width="1.5"/><rect x="64" y="1" width="12" height="12" fill="#333" transform="rotate(45 70 7)"/></svg>
<div class="abs avatar" role="img" aria-label="Guest portrait"></div>
<div class="abs person">Dane Morrow</div>
<p class="abs quote">" The Staff was very professional, patient &amp; friendly.. The Service was very good &amp; thorough.. Marla did a great job of cleaning my teeth.. Janine (as always) &amp; the office personnel took complete care of my insurance &amp; administrative needs.. And of course, I just Love Dr. Hale!! She's The Best!! Overall great 1st visit.. I will be back &amp; refer friends.. I really like the new office &amp; location.. Thank you ALL &amp; Many Blessings!! "</p>

<div class="abs footer"></div>
<div class="abs footer-brand">Corriveld</div>
<div class="abs fcol" style="left:150px">
  <svg width="18" height="26" viewBox="0 0 18 26"><path d="M9 0C4 0 0 4 0 9c0 7 9 17 9 17s9-10 9-17C18 4 14 0 9 0z" fill="#999"/><circle cx="9" cy="9" r="3.5" fill="#050505"/></svg>
  <div><h4>HOSPITAL ADDRESS</h4>12 Wattle Lane, Hill Corner<br>Ballarat - 3350</div>
</div>
<div class="abs fcol" style="left:492px">
  <svg width="22" height="22" viewBox="0 0 24 24"><path d="M6.6 10.8a15 15 0 006.6 6.6l2.2-2.2c.3-.3.7-.4 1-.2 1.1.4 2.3.6 3.6.6.6 0 1 .4 1 1V20c0 .6-.4 1-1 1A17 17 0 013 4c0-.6.4-1 1-1h3.5c.6 0 1 .4 1 1 0 1.3.2 2.5.6 3.6.1.3 0 .7-.2 1z" fill="#999"/></svg>
  <div><h4>EMERGENCY ( 24X7 )</h4>(+1)800 555 019<br>Call Us Now- 24/7 Customer Support</div>
</div>
<div class="abs fcol" style="left:862px">
  <svg width="26" height="20" viewBox="0 0 26 20"><rect x="1" y="1" width="24" height="18" fill="none" stroke="#999" stroke-width="2"/><path d="M1 1l12 10L25 1" fill="none" stroke="#999" stroke-width="2"/></svg>
  <div><h4>HOSPITAL ADDRESS</h4>info@corriveldhouse.com<br>stay@corriveldhouse.com</div>
</div>
<div class="abs legal">Copyright © 2015 Corriveld. All Rights Reserved | Sitemap</div>

</body>
</html>
```